Finch Essential Oils - Body Oils

I am in need of 4 different label and package designs for a new line of body oils that I am launching. I already have the logo and names, it is now a matter of positioning the content. The names are as follows;

1) CARDAMOM + CYPRESS
WARMING BODY OIL
2) NEROLI + LEMON
UPLIFTING BODY OIL
3) CEDAR + BIRCH
GROUNDING BODY OIL
4) SAGE + MINT
COOLING BODY OIL.
The size of each label is 13cm wide x 9.5cm high. The size of the box is 4.5cm x 4.5cm x 15.5cm high.
The size of the bottle is 4cm across the base and 10.5cm in glass height.
I have included an image from a line that I started to work on but it didn't go anywhere. I thought the borders looked good to frame it in however, I am not attached to anything at this point. I am also including a picture of a product line that has used different colors on the packaging. I am not certain that this is the direction I'd like to take however I like how it looks with them. If we were to add the color I think it should be JUST the boxes and NOT the labels and they would be as follows; WARMING OIL - warm burgundy, earth tones UPLIFTING OIL - warm light, lightish blues GROUNDING OIL - warm soft, brownish creams COOLING OIL - refreshing light, pale green possibly blue. I would be interested to see what adding a sprig of a plant would look like on the boxes however with the already busy logo it might look like too much is going on. As you will see in our instagram and website we currently have the bear logo in a foil. I am not sure that I want to proceed with this foil as it is difficult to photograph. I would like to look at colors that compliment the existing line of essential oils as well as the dark brown wood on the cap.
I have added a design that looks a bit industrial that I like, it reads black ops.

Target Market(s)

My market is mainly females who are interested in natural health age 17 - 70. There is a large movement for organic + green beauty. I would like the label to look and feel clean and natural. Something that has been wildcrafted, raw and completely from nature.

Industry/Entity Type

Health And Wellness

Colors

Designer to choose colors to be used in the design.

Requirements
Must have
• Appeal to very progressive organic consumers. Please see the pictures marked SAMPLES 1, 2, 3 + 4 for design ideas.
• Easy to read. Clean design.
• The following information should be on the label as well as the packaging box.
• Size - 100 ML
• Barcodes - still to come
• Ingredients:
• 1) CARDAMOM + CYPRESS WARMING BODY OIL - *Sunflower Oil, **Orange, **Cardamom, **Cypress, **Ginger *Organic, **Organic essential oil
• 2) NEROLI + LEMON UPLIFTING BODY OIL - *Sunflower oil, **Orange, **Neroli, **Grapefruit, **Lemon, **Bergamot, **Benzoin, *Organic, **Organic essential oil
• 3) CEDAR + BIRCH GROUNDING BODY OIL - *Sunflower Oil, **Cedarwood, **Birch, **Benzoin, **Patchouli,*Organic, **Organic essential oil
• 4) SAGE + MINT COOLING BODY OIL - *Sunflower oil, **Spearmint, **Clary Sage, **Geranium, **Ylang Ylang, *Organic, **Organic essential oil
• Suggested Use:
• Warm oil if desired. Apply to the full body after bathing, massage in motions toward the heart until the oil is mostly absorbed. Can also be added to bath water.
Nice to have
• I would like to see the designs on the actual bottle (pic included) to see how it looks.
Should not have
• Bright colors.

```html
<!DOCTYPE html>
<html lang="en">
<head>
<meta charset="utf-8">
<title>Finch Essential Oils – Cardamom + Cypress Label</title>
<link href="https://fonts.googleapis.com/css2?family=Share+Tech+Mono&display=swap" rel="stylesheet">
<style>
  :root {
    --backdrop: #d7d7d7;
    --paper-white: #f7f6f2;
    --paper-kraft: #b6a189;
    --ink: #2f1f1a;
    --ink-soft: #4a3a33;
  }
  * { margin: 0; padding: 0; box-sizing: border-box; }
  html, body {
    width: 857px; height: 1200px; overflow: hidden;
    background: var(--backdrop);
  }
  body {
    position: relative;
    font-family: "Share Tech Mono", monospace;
    color: var(--ink);
  }
  .label {
    position: absolute;
    left: 64px;
    width: 719px; height: 526px;
    background: var(--paper-white);
  }
  .label--white { top: 62px; }
  .label--kraft { top: 618px; background: var(--paper-kraft); }

  .label__usage {
    position: absolute;
    left: 24px; top: 482px;
    width: 464px;
    transform: rotate(-90deg);
    transform-origin: top left;
    font-size: 10.5px;
    line-height: 16px;
    letter-spacing: 0.2px;
    text-transform: uppercase;
    color: var(--ink-soft);
  }
  .label__ingredients { margin-top: 12px; }

  .label__brand {
    position: absolute;
    left: 206px; top: 42px;
    width: 306px; height: 184px;
    display: flex; flex-direction: column;
    align-items: center; justify-content: center; gap: 14px;
    text-align: center;
    font-size: 24px; letter-spacing: 3px; line-height: 1.3;
    text-transform: uppercase;
  }
  .label__brand-square {
    width: 18px; height: 18px; background: var(--ink);
  }

  .label__rule {
    position: absolute; left: 206px; width: 308px;
    height: 1.5px; background: var(--ink);
  }
  .label__text {
    position: absolute; left: 208px;
    text-transform: uppercase; white-space: nowrap;
  }
  .label__title { font-size: 25px; letter-spacing: 1px; }
  .label__title--scent { top: 262px; }
  .label__title--type { top: 310px; }
  .label__subtitle { top: 362px; font-size: 19px; letter-spacing: 1px; color: var(--ink-soft); }
  .label__claim { top: 404px; font-size: 15.5px; line-height: 23px; letter-spacing: 0.5px; color: var(--ink-soft); }

  .label__divider {
    position: absolute; left: 445px; top: 404px;
    width: 1.5px; height: 66px; background: var(--ink);
  }
  .label__size {
    position: absolute; left: 484px; top: 437px;
    transform: translate(-50%, -50%) rotate(-90deg);
    font-size: 22px; letter-spacing: 1px;
  }

  .label__barcode-area {
    position: absolute; left: 582px; top: 44px;
    width: 106px; height: 438px;
    border: 1.5px solid var(--ink);
  }
  .label__web {
    position: absolute; left: 672px; top: 270px;
    transform: translate(-50%, -50%) rotate(-90deg);
    font-size: 10.5px; letter-spacing: 1px;
    text-transform: uppercase; white-space: nowrap;
  }
</style>
</head>
<body>

  <section class="label label--white" aria-label="Warming body oil label, white stock">
    <div class="label__usage">
      <p>Suggested use:</p>
      <p>Warm oil if desired. Apply to the full body after bathing, massage in motions toward the heart until the oil is mostly absorbed. Can also be added to bath water.</p>
      <p class="label__ingredients">*Sunflower oil, **Orange, **Cardamom, **Cypress, **Ginger *Organic, **Organic essential oil</p>
    </div>
    <div class="label__brand"><span class="label__brand-square"></span>Finch<br>Essential Oils</div>
    <p class="label__text label__title label__title--scent">Cardamom + Cypress</p>
    <div class="label__rule" style="top:303px"></div>
    <p class="label__text label__title label__title--type">Warming Body Oil</p>
    <div class="label__rule" style="top:349px"></div>
    <p class="label__text label__subtitle">Organic Botanicals</p>
    <div class="label__rule" style="top:393px"></div>
    <p class="label__text label__claim">Revitalizing and<br>stimulating for a<br>renewed sense of spirit</p>
    <div class="label__divider"></div>
    <p class="label__size">100ML</p>
    <div class="label__rule" style="top:482px"></div>
    <div class="label__barcode-area"></div>
    <p class="label__web">www.finchessentialoils.com</p>
  </section>

  <section class="label label--kraft" aria-label="Warming body oil label, kraft stock">
    <div class="label__usage">
      <p>Suggested use:</p>
      <p>Warm oil if desired. Apply to the full body after bathing, massage in motions toward the heart until the oil is mostly absorbed. Can also be added to bath water.</p>
      <p class="label__ingredients">*Sunflower oil, **Orange, **Cardamom, **Cypress, **Ginger *Organic, **Organic essential oil</p>
    </div>
    <div class="label__brand"><span class="label__brand-square"></span>Finch<br>Essential Oils</div>
    <p class="label__text label__title label__title--scent">Cardamom + Cypress</p>
    <div class="label__rule" style="top:303px"></div>
    <p class="label__text label__title label__title--type">Warming Body Oil</p>
    <div class="label__rule" style="top:349px"></div>
    <p class="label__text label__subtitle">Organic Botanicals</p>
    <div class="label__rule" style="top:393px"></div>
    <p class="label__text label__claim">Revitalizing and<br>stimulating for a<br>renewed sense of spirit</p>
    <div class="label__divider"></div>
    <p class="label__size">100ML</p>
    <div class="label__rule" style="top:482px"></div>
    <div class="label__barcode-area"></div>
    <p class="label__web">www.finchessentialoils.com</p>
  </section>

</body>
</html>
```